Beacon for the Peoples Magazine Ad

I need a magazine Ad designed today! The deadline is March 31. The add is for a religious non profit called "beacon for the peoples."

The add will be fairly simple but will include a stock photo of a syrian refugee (preferably looking to the camera) and will include the title of the organization -
"Beacon for the Peoples"
and the slogan - "Partnering with you to change the world"

Somewhere on or near the picture it will say "because we are the church."
to the side there will be a small section that will say "visit our booth and register to win a free pomelo band" and we will have a picture of an pomelo band active

These are the specs for the piece -
Half Page Magazine Ad: Deadline March 31
 • Full Bleed Size: 8.25"w x 4.25"h
 • Trim Size: 8"w x 4"h
 • Live Area: 7.5"w x 3.5"h
 • PDF, JPG, AI, PSD and TIFF files accepted at 300dpi 

Please see the attached files -
We wish to use MONTSERRAT font for the "Beacon for the Peoples."
We like Black, White, Yellow, and maybe a green & or blue (brazil colors)
We like slashes and also triangle shapes and things that are partially shaded. We also like things with various different text sizes etc.

Please be creative ... Thanks!

Target Market(s)

Church Leaders

Industry/Entity Type

Religious

Font styles to use
Other font styles liked:
• montserrat

Colors
fbed22
ffffff

Requirements
Must have
• Stock Photo of Syrian refugee child
Should not have
• Crosses or traditional religious symbols

```html
<!DOCTYPE html>
<html lang="en">
<head>
<meta charset="utf-8">
<title>Beacon for the Peoples – Magazine Ad</title>
<link rel="stylesheet" href="https://fonts.googleapis.com/css2?family=Montserrat:wght@500;600&family=Roboto+Condensed:wght@400&family=Cormorant+Garamond:ital,wght@1,600;1,700&display=swap">
<style>
  :root {
    --page: #ffffff;
    --rule: #a7a7a7;
    --ink: #111111;
    --title-light: #e3e4e6;
    --white: #ffffff;
    --yellow: #fbd422;
    --grey-mid: #8b8c8f;
    --grey-dark: #3c3c3e;
    --pill: rgba(225, 226, 228, 0.85);
  }
  * { margin: 0; padding: 0; box-sizing: border-box; }
  html, body { width: 1200px; height: 1002px; overflow: hidden; background: var(--page); }
  .page { position: relative; width: 1200px; height: 1002px; border-top: 2px solid var(--rule); }
  .ad {
    position: absolute; left: 39px; top: 235px; width: 1122px; height: 561px;
    overflow: hidden;
    background: linear-gradient(90deg, #cfd0d2 0%, var(--grey-mid) 45%, #7b7c7f 80%, var(--grey-dark) 100%);
  }
  .beams { position: absolute; inset: 0; }
  .photo {
    position: absolute; left: 0; top: 0; width: 500px; height: 561px;
    background: linear-gradient(90deg, #8a6a55 0%, #c49a7a 35%, #eddcc6 70%, rgba(235,230,225,0) 100%);
  }
  .tagline {
    position: absolute; left: 318px; top: 256px; width: 142px;
    font: 400 20px/1.22 "Roboto Condensed", sans-serif; color: var(--ink);
    text-align: center; letter-spacing: 0.3px;
  }
  .title { position: absolute; left: 490px; top: 80px; width: 560px; font-family: "Montserrat", sans-serif; text-align: center; }
  .title-main { display: block; font-weight: 500; font-size: 128px; line-height: 1; color: var(--title-light); letter-spacing: -2px; }
  .title-sub { display: block; margin-top: 28px; font-weight: 500; font-size: 46px; line-height: 1; color: var(--white); letter-spacing: 0.5px; }
  .slogan { position: absolute; left: 560px; top: 330px; width: 490px; text-align: center; font-family: "Cormorant Garamond", serif; font-style: italic; }
  .slogan-lead { display: block; font-weight: 600; font-size: 36px; line-height: 1.05; color: var(--ink); }
  .slogan-accent { display: block; font-weight: 700; font-size: 40px; line-height: 1.05; color: var(--yellow); text-transform: uppercase; }
  .promo {
    position: absolute; left: 571px; top: 495px; width: 560px; height: 44px;
    background: var(--pill); border-radius: 22px 0 0 22px;
    display: flex; align-items: center; padding-left: 10px;
    font: 400 19px/1 "Roboto Condensed", sans-serif; color: var(--ink);
  }
  .promo-product {
    position: absolute; left: 458px; top: 2px; width: 36px; height: 40px;
    border-radius: 9px; background: linear-gradient(160deg, #4a4b4d, #141415);
  }
</style>
</head>
<body>
<div class="page">
  <section class="ad">
    <svg class="beams" width="1122" height="561" viewBox="0 0 1122 561" aria-hidden="true">
      <polygon points="400,40 1122,0 1122,30" fill="#ffffff" opacity="0.12"/>
      <polygon points="380,80 1122,190 1122,260" fill="#ffffff" opacity="0.14"/>
      <polygon points="420,290 1122,180 1122,240" fill="#ffffff" opacity="0.12"/>
      <polygon points="430,340 1122,400 1122,470" fill="#ffffff" opacity="0.10"/>
      <polygon points="440,470 1122,561 820,561" fill="#ffffff" opacity="0.14"/>
      <polygon points="500,0 980,0 520,30" fill="#000000" opacity="0.18"/>
    </svg>
    <div class="photo" role="img" aria-label="Stock photo of a refugee child looking to the camera through a chain-link fence"></div>
    <p class="tagline">BECAUSE WE ARE THE CHURCH</p>
    <h1 class="title">
      <span class="title-main">BEACON</span>
      <span class="title-sub">FOR THE PEOPLES</span>
    </h1>
    <p class="slogan">
      <span class="slogan-lead">Partnering with you to</span>
      <span class="slogan-accent">Change the World</span>
    </p>
    <div class="promo">
      Visit our booth and register to win a free POMELO BAND
      <div class="promo-product" role="img" aria-label="Product photo of a Pomelo Band Active smartwatch"></div>
    </div>
  </section>
</div>
</body>
</html>
```